依頼詳細
頂いている参考サイトとしては下記のURLがありますが、
先方でもどのデザインの何が良いのかは計りかねているらしく、
下記を参考に様々な形式でデザインを作成して欲しいということです。

‣BRIGHTLEAF https://www.brightleaf57.jp/biwako-sup/ ➡デザインが素敵
‣丸岡商 https://www.maruokasho.co.jp/ja/ ➡ 大企業感
‣ひらめき工房本部 https://www.hiramekikobo.jp/  ➡ 同コンセプト

また、事業内容は現在のページに準拠するということで、現在サイトのパスはpemixとなります。

TOPページへの掲載内容については、
TOPイメージ
事業内容
採用情報
新着情報
となります。
サイトURL
http://nexal.co.jp/
ページ数
1ページ
希望イメージ
シンプル 複雑
単色 カラフル
暗い 明るい
日常 高級
遊び心 厳粛
未来的 伝統的
女性的 男性的
希望する色
緑系
納品ファイル
• フォトショップ形式 (.psd)
補足説明
依頼公開後の追記内容
現行サイトのパスワードについて失念しておりました。
パスワードは pemix となります。
■ 選んだ理由

デザインが特に先方に気に入られたため

■ 提案者全員のお礼・コメント

この度はご提案をいただきまして、誠にありがとうございました。
また機会がありましたら、よろしくお願い致します。

```html
<!DOCTYPE html>
<html lang="ja">
<head>
<meta charset="UTF-8">
<title>株式会社ネクサル</title>
<link href="https://fonts.googleapis.com/css2?family=Jost:wght@400;500;600&family=Noto+Sans+JP:wght@400;500;700&display=swap" rel="stylesheet">
<style>
:root{
  --navy:#1c202b;
  --navy-deep:#161a23;
  --green:#7ccc3c;
  --white:#ffffff;
  --ink:#222631;
  --muted:#666b75;
  --gray-bg:#f2f3f4;
  --rule:#dcdee1;
}
*{margin:0;padding:0;box-sizing:border-box}
html,body{width:1200px;height:2496px;overflow:hidden}
body{font-family:"Noto Sans JP",sans-serif;color:var(--ink);background:var(--white);position:relative}
.en{font-family:"Jost",sans-serif}
.photo{position:absolute}

/* hero */
.hero{position:absolute;left:0;top:0;width:1200px;height:640px;background:var(--navy)}
.brand{position:absolute;left:56px;top:24px;color:var(--white);display:flex;align-items:baseline;gap:12px}
.brand-en{font-family:"Jost",sans-serif;font-size:20px;font-weight:600;letter-spacing:.04em}
.brand-jp{font-size:13px;font-weight:500}
.nav{position:absolute;right:48px;top:22px;display:flex;gap:34px}
.nav a{color:var(--white);text-decoration:none;text-align:center;font-family:"Jost",sans-serif;font-size:15px;font-weight:500;letter-spacing:.05em;line-height:1.1}
.nav a small{display:block;font-family:"Noto Sans JP",sans-serif;font-size:9px;font-weight:400;opacity:.75;letter-spacing:0}
.hero-photo{left:600px;top:132px;width:528px;height:396px;background:linear-gradient(135deg,#e9ecef,#c6ccd3 60%,#8d95a1)}
.hero-title{position:absolute;left:56px;top:270px;color:var(--white);font-family:"Jost",sans-serif;font-size:30px;font-weight:500;line-height:1.4}
.hero-lead{position:absolute;left:56px;top:372px;color:var(--white);font-size:14px;opacity:.85}
.more{position:absolute;display:flex;align-items:center;gap:12px;font-family:"Jost",sans-serif;font-size:14px;font-weight:500;letter-spacing:.05em;text-decoration:none}
.more .line{width:40px;height:2px;background:var(--green);position:relative}
.more .line::after{content:"";position:absolute;right:-6px;top:-5px;width:12px;height:12px;border-radius:50%;background:var(--green)}
.hero .more{left:56px;top:436px;color:var(--white)}

/* section heads */
.label{position:absolute;font-family:"Jost",sans-serif;color:var(--green);font-size:13px;font-weight:500;letter-spacing:.12em}
.heading{position:absolute;font-size:40px;font-weight:700;color:var(--ink);line-height:1.2}

/* business */
.biz-band{position:absolute;left:0;top:1132px;width:1200px;height:292px;background:var(--green)}
.biz-left{left:68px;top:856px;width:492px;height:272px;background:linear-gradient(160deg,#f0f0f0,#c9c9cc 55%,#3b3e46)}
.biz-right{left:632px;top:928px;width:500px;height:312px;background:linear-gradient(180deg,#9cc3e6 0%,#c6dcef 40%,#a39e8c 70%,#6b6b6d)}
.biz-card{position:absolute;color:var(--white)}
.biz-card h3{font-size:17px;font-weight:700;display:flex;align-items:center;gap:14px;margin-bottom:12px}
.biz-card h3 .line{width:36px;height:2px;background:var(--white)}
.biz-card p{font-size:12px;line-height:1.8}
.biz-card.edu{left:68px;top:1200px;width:500px}
.biz-card.jpn{left:632px;top:1284px;width:500px}

/* recruit */
.recruit-sub{position:absolute;left:56px;top:1690px;font-size:20px;font-weight:700}
.recruit-text{position:absolute;left:56px;top:1740px;width:470px;font-size:13px;line-height:1.8;color:var(--muted)}
.recruit .more{left:56px;top:1926px;color:var(--ink)}
.r1{left:600px;top:1432px;width:248px;height:256px;background:linear-gradient(135deg,#d8d9db,#a9acb3)}
.r2{left:868px;top:1556px;width:264px;height:264px;background:linear-gradient(135deg,#eceae6,#b8bcc4)}
.r3{left:600px;top:1708px;width:248px;height:272px;background:linear-gradient(135deg,#9a8f84,#5c6470)}
.r4{left:868px;top:1836px;width:264px;height:264px;background:linear-gradient(135deg,#f1eee9,#d9c7b8)}

/* news */
.news{position:absolute;left:0;top:2140px;width:1200px;height:300px;background:var(--gray-bg)}
.news-list{position:absolute;left:400px;top:80px;width:740px;list-style:none}
.news-list li{display:flex;gap:24px;font-size:13px;padding:14px 0;border-bottom:1px solid var(--rule)}
.news-list time{color:var(--muted)}
.news-list a{color:var(--ink);text-decoration:underline}
.footer{position:absolute;left:0;top:2440px;width:1200px;height:56px;background:var(--navy-deep);color:var(--white);font-size:11px;display:flex;align-items:center;justify-content:center}
</style>
</head>
<body>

<section class="hero">
  <div class="brand"><span class="brand-en">NEXAL</span><span class="brand-jp">株式会社ネクサル</span></div>
  <nav class="nav">
    <a href="#">ABOUT<small>会社概要</small></a>
    <a href="#">BUSINESS<small>事業内容</small></a>
    <a href="#">RECRUIT<small>採用情報</small></a>
    <a href="#">CONTACT<small>お問い合わせ</small></a>
  </nav>
  <div class="photo hero-photo" role="img" aria-label="机で学ぶ制服姿の学生の写真"></div>
  <h1 class="hero-title">Growing Knowledge with Passion<br>and Trust shapes a Brighter Tomorrow.</h1>
  <p class="hero-lead">好奇心と勇気を合わせた知が、未来を永遠につなげる</p>
  <a class="more" href="#">MORE<span class="line"></span></a>
</section>

<section class="business">
  <div class="biz-band"></div>
  <span class="label" style="left:56px;top:744px;">BUSINESS</span>
  <h2 class="heading" style="left:56px;top:772px;">事業内容</h2>
  <div class="photo biz-left" role="img" aria-label="ノートに書き込みながら学習する手元の写真"></div>
  <div class="photo biz-right" role="img" aria-label="海外の街並みと三輪タクシーの写真"></div>
  <div class="biz-card edu">
    <h3>教育事業部<span class="line"></span></h3>
    <p>一人ひとりの個性と可能性を大切にし、学ぶ楽しさを届ける教室を運営しています。<br>地域に根ざした学びの場で、子どもたちの成長を全力で支えます。</p>
  </div>
  <div class="biz-card jpn">
    <h3>日本事業部<span class="line"></span></h3>
    <p>海外の皆様に日本の文化や教育の魅力を伝え、新たな交流を生み出しています。<br>国や言葉をこえた学びの機会を、これからも広げていきます。</p>
  </div>
</section>

<section class="recruit">
  <span class="label" style="left:56px;top:1504px;">RECRUIT</span>
  <h2 class="heading" style="left:56px;top:1590px;">採用情報</h2>
  <div class="photo r1" role="img" aria-label="書類を前に話し合う手元の写真"></div>
  <div class="photo r2" role="img" aria-label="スーツ姿で資料を持つ社員の写真"></div>
  <div class="photo r3" role="img" aria-label="教室で学ぶ生徒たちの写真"></div>
  <div class="photo r4" role="img" aria-label="カラフルな文具と資料の写真"></div>
  <h3 class="recruit-sub">人の成長を応援したい</h3>
  <p class="recruit-text">私たちは一緒に働く仲間を募集しています。人の成長に寄り添い、共に未来をつくりたい方からのご応募をお待ちしています。</p>
  <a class="more" href="#">MORE<span class="line"></span></a>
</section>

<section class="news">
  <span class="label" style="left:56px;top:92px;">NEWS</span>
  <h2 class="heading" style="left:56px;top:120px;">お知らせ</h2>
  <ul class="news-list">
    <li><time class="en">2020.12.14</time><a href="#">この文章はダミーです。新しいお知らせの内容がここに入ります。</a></li>
    <li><time class="en">2020.12.14</time><a href="#">この文章はダミーです。新しいお知らせの内容がここに入ります。</a></li>
    <li><time class="en">2020.12.14</time><a href="#">この文章はダミーです。新しいお知らせの内容がここに入ります。</a></li>
  </ul>
</section>

<footer class="footer">Copyright © 2020 株式会社NEXAL. All rights reserved.</footer>

</body>
</html>
```